Logo with Stationery Design Project-

The company is an on-line service for assisting the people that are in a foreclosure situation with their homes. We are presently building the site on NestPlume with Wordpress.

The best option to save a home in the USA at the end of the line with the banks is to file for bankruptcy Chapter 7 or Chapter 13. We work with homeowners and attorneys to prepare the financial package for the attorneys to negotiate with the banks after filing for bankruptcy. We also sell a binder on-line which is called the hearthsafe renewal binder and the web site is: www.hearthsaferenewalbinder.example
We need a logo and stationnary to communicate the message of advisors in the field of financial strategies when it comes to the foreclosure and bankruptcy process. This stationnary will be printed on high quality paper with the business cards being on 100 stock which is high quality in the USA.

We would like to see the logo to use the Navy blue and Aqua Green colors. The final desing should communicate the financial knowledge and promise of a light at the end of the tunnell.

The card should use both sides with the back side being the logo and the web site address that links with the front of the card. Letterhead and envelopes should be serious but sexy!

A challenge that I am sure someone is up to........

12 million people that are in foreclosure in the USA and all of the law firms that deal with foreclosure and bankruptcies in the USA all 50 states

Financial

• Colors are important = Navy blue and Aqua green

```html
<!DOCTYPE html>
<html lang="en">
<head>
<meta charset="utf-8">
<title>Hearthsafe Stationery</title>
<link rel="stylesheet" href="https://fonts.googleapis.com/css2?family=Open+Sans:wght@400;600&display=swap">
<style>
  :root {
    --desk: #c3b59a;
    --paper: #ffffff;
    --navy: #1d3f7a;
    --ink: #1a2233;
    --aqua: #2a9595;
    --aqua-light: #3aa7a5;
    --env-deep: #0f3458;
    --env-mid: #1a5079;
    --env-line: #5fb8c4;
  }
  * { margin: 0; padding: 0; box-sizing: border-box; }
  html, body { width: 1200px; height: 848px; overflow: hidden; }
  body {
    background: var(--desk);
    font-family: "Open Sans", Arial, sans-serif;
    position: relative;
  }
  .letter {
    position: absolute;
    width: 507px;
    height: 717px;
    background: var(--paper);
    color: var(--ink);
    box-shadow: 0 1px 3px rgba(0,0,0,.12);
    overflow: hidden;
  }
  .letter--tilted { transform: rotate(-19.6deg); transform-origin: 50% 50%; }
  .letter--back  { left: -21px; top: -113px; }
  .letter--mid   { left: 107px; top: 8px; }
  .letter--front { left: 236px; top: 129px; }
  .letter--upright { left: 770px; top: 103px; transform: scale(.803); transform-origin: 0 0; }

  .letter__brand {
    position: absolute; left: 22px; top: 46px;
    display: flex; align-items: center; gap: 7px;
    font-size: 17px; font-weight: 600; color: var(--navy);
  }
  .letter__brand-mark { width: 14px; height: 14px; background: var(--navy); }
  .letter__tagline {
    position: absolute; right: 20px; top: 52px;
    font-size: 15px; color: var(--navy);
  }
  .letter__band {
    position: absolute; left: 0; right: 0; top: 77px; height: 13px;
    background: var(--aqua);
  }
  .letter__date {
    position: absolute; right: 70px; top: 116px; font-size: 11px;
  }
  .letter__greeting {
    position: absolute; left: 46px; top: 206px; font-size: 11px;
  }
  .letter__body {
    position: absolute; left: 46px; top: 248px;
    font-size: 9.6px; line-height: 1.5;
    white-space: nowrap;
  }
  .letter__closing {
    position: absolute; right: 40px; top: 430px; font-size: 11px;
  }
  .letter__web {
    position: absolute; left: 120px; bottom: 16px;
    font-size: 9.5px; color: var(--navy);
  }

  .envelope {
    position: absolute; left: 751px; top: 442px; width: 439px; height: 300px;
  }
  .envelope__flap {
    position: absolute; left: 0; top: 0; width: 100%; height: 90px;
    background: var(--aqua-light);
    border-radius: 40px 40px 0 0;
  }
  .envelope__body {
    position: absolute; left: 0; top: 52px; width: 100%; height: 248px;
    background: radial-gradient(ellipse at 40% 35%, var(--env-mid) 0%, var(--env-deep) 75%);
  }
  .envelope__band {
    position: absolute; left: 0; right: 0; top: 263px; height: 14px;
    background: var(--aqua);
  }
  .envelope__address {
    position: absolute; left: 216px; width: 193px; height: 1px;
    background: var(--env-line); opacity: .8;
  }
  .envelope__address--1 { top: 171px; }
  .envelope__address--2 { top: 198px; }
  .envelope__address--3 { top: 225px; }
  .envelope__brand {
    position: absolute; left: 22px; top: 240px;
    display: flex; align-items: center; gap: 6px;
    font-size: 9px; color: var(--aqua-light);
  }
  .envelope__brand-mark { width: 10px; height: 10px; background: var(--aqua-light); }
</style>
</head>
<body>

<article class="letter letter--tilted letter--back">
  <div class="letter__brand"><span class="letter__brand-mark"></span>Hearthsafe</div>
  <div class="letter__tagline">Save your home with us!</div>
  <div class="letter__band"></div>
  <div class="letter__date">City, 24.10.2011.</div>
  <div class="letter__greeting">Dear,</div>
  <p class="letter__body">Lorem Ipsum is simply dummy text of the printing and typesetting industry.<br>Lorem Ipsum has been the industry's standard dummy text ever since the 1500s,<br>when an unknown printer took a galley of type and scrambled it to make a type specimen<br>book. It has survived not only five centuries, but also the leap into electronic<br>typesetting, remaining essentially unchanged. It was popularised in<br>the 1960s with the release of Letraset sheets containing Lorem Ipsum<br>passages, and more recently with desktop publishing software like<br>Aldus PageMaker including versions of Lorem Ipsum.</p>
  <div class="letter__closing">Best Regards!</div>
  <div class="letter__web">www.hearthsaferenewalbinder.example</div>
</article>

<article class="letter letter--tilted letter--mid">
  <div class="letter__brand"><span class="letter__brand-mark"></span>Hearthsafe</div>
  <div class="letter__tagline">Save your home with us!</div>
  <div class="letter__band"></div>
  <div class="letter__date">City, 24.10.2011.</div>
  <div class="letter__greeting">Dear,</div>
  <p class="letter__body">Lorem Ipsum is simply dummy text of the printing and typesetting industry.<br>Lorem Ipsum has been the industry's standard dummy text ever since the 1500s,<br>when an unknown printer took a galley of type and scrambled it to make a type specimen<br>book. It has survived not only five centuries, but also the leap into electronic<br>typesetting, remaining essentially unchanged. It was popularised in<br>the 1960s with the release of Letraset sheets containing Lorem Ipsum<br>passages, and more recently with desktop publishing software like<br>Aldus PageMaker including versions of Lorem Ipsum.</p>
  <div class="letter__closing">Best Regards!</div>
  <div class="letter__web">www.hearthsaferenewalbinder.example</div>
</article>

<article class="letter letter--tilted letter--front">
  <div class="letter__brand"><span class="letter__brand-mark"></span>Hearthsafe</div>
  <div class="letter__tagline">Save your home with us!</div>
  <div class="letter__band"></div>
  <div class="letter__date">City, 24.10.2011.</div>
  <div class="letter__greeting">Dear,</div>
  <p class="letter__body">Lorem Ipsum is simply dummy text of the printing and typesetting industry.<br>Lorem Ipsum has been the industry's standard dummy text ever since the 1500s,<br>when an unknown printer took a galley of type and scrambled it to make a type specimen<br>book. It has survived not only five centuries, but also the leap into electronic<br>typesetting, remaining essentially unchanged. It was popularised in<br>the 1960s with the release of Letraset sheets containing Lorem Ipsum<br>passages, and more recently with desktop publishing software like<br>Aldus PageMaker including versions of Lorem Ipsum.</p>
  <div class="letter__closing">Best Regards!</div>
  <div class="letter__web">www.hearthsaferenewalbinder.example</div>
</article>

<article class="letter letter--upright">
  <div class="letter__brand"><span class="letter__brand-mark"></span>Hearthsafe</div>
  <div class="letter__tagline">Save your home with us!</div>
  <div class="letter__band"></div>
  <div class="letter__date">City, 24.10.2011.</div>
  <div class="letter__greeting">Dear,</div>
  <p class="letter__body">Lorem Ipsum is simply dummy text of the printing and typesetting industry.<br>Lorem Ipsum has been the industry's standard dummy text ever since the 1500s,<br>when an unknown printer took a galley of type and scrambled it to make a type specimen<br>book. It has survived not only five centuries, but also the leap into electronic<br>typesetting, remaining essentially unchanged. It was popularised in<br>the 1960s with the release of Letraset sheets containing Lorem Ipsum<br>passages, and more recently with desktop publishing software like<br>Aldus PageMaker including versions of Lorem Ipsum.</p>
</article>

<section class="envelope">
  <div class="envelope__body"></div>
  <div class="envelope__flap"></div>
  <div class="envelope__address envelope__address--1"></div>
  <div class="envelope__address envelope__address--2"></div>
  <div class="envelope__address envelope__address--3"></div>
  <div class="envelope__brand"><span class="envelope__brand-mark"></span>www.hearthsaferenewalbinder.example</div>
  <div class="envelope__band"></div>
</section>

</body>
</html>
```